Lorna Tess Tresses Fancy Business Card’s

I want my business cards to be elite, original and very classy. I want the business cards to match the colors of my logo and to match the design posted. I would love the design of the picture I posted

I want the card all white .
The dripping on the top of the card I want it to match the pink color in my logo that’s also posted .
I need my logo on the business card !
I need my Instagram- @lorna.tess.tresses__
And my phone number - 582 907 3365

Target Market(s)

My target market is young woman age 23 to older woman to the age of 65
I want both older and younger women to love my design . I don’t want any cheap looking business cards

Industry/Entity Type

Hair And Beauty

Contact Information for Business Card

Add my logo
Add my Instagram- @lorna.tess.tresses__
My number - 582 907 3365
My website- www.lornatesstresses.example

Font styles to use
Serif
Script

Colors
ffffff
e667a6
e34298

Requirements
Must have
• The business cards must have my logo, my number , my website, and my Instagram!
Nice to have
• Nice to have glitter words that match my logo
• The business cards must look classy and mature
• I want them to be very unique!!
Should not have
• Should not have any colors that doesn’t match my logo ! This is very important! Please

```html
<!DOCTYPE html>
<html lang="en">
<head>
<meta charset="utf-8">
<title>Lorna Tess Tresses – Business Card</title>
<link href="https://fonts.googleapis.com/css2?family=Roboto:wght@400;500&family=Playball&display=swap" rel="stylesheet">
<style>
  :root {
    --pink: #e667a6;
    --pink-deep: #e34298;
    --white: #ffffff;
    --ink: #3c3c3c;
    --grey: #8a8a8a;
    --stage: #4a4a4a;
  }
  * { margin: 0; padding: 0; box-sizing: border-box; }
  html, body {
    width: 1200px; height: 1200px; overflow: hidden;
    background: var(--stage);
    font-family: "Roboto", Arial, sans-serif;
  }
  .sheet {
    width: 1200px; height: 1200px;
    display: flex; flex-direction: column; align-items: center; justify-content: center;
    gap: 60px;
  }
  .card {
    width: 840px; height: 480px;
    border-radius: 26px;
    position: relative;
    overflow: hidden;
  }
  .card--front { background: var(--pink); display: flex; align-items: center; justify-content: center; }
  .card--back { background: var(--white); display: flex; align-items: center; justify-content: center; }

  .brand-name {
    font-family: "Roboto", Arial, sans-serif;
    font-weight: 400;
    letter-spacing: 0.12em;
    text-transform: uppercase;
    text-align: center;
    line-height: 1.25;
  }
  .card--front .brand-name { color: var(--white); font-size: 48px; }
  .card--back .brand-name { color: var(--pink-deep); font-size: 30px; width: 300px; }

  .divider {
    width: 2px; height: 230px;
    background: linear-gradient(var(--white), var(--pink-deep), var(--white));
    margin: 0 44px;
  }
  .contact { color: var(--ink); }
  .contact__name {
    font-family: "Playball", cursive;
    font-size: 40px; line-height: 1;
  }
  .contact__name .first { color: var(--pink-deep); }
  .contact__name .last { color: var(--grey); }
  .contact__role { font-size: 26px; margin: 6px 0 26px; }
  .contact__list { list-style: none; }
  .contact__item {
    display: flex; align-items: center; gap: 10px;
    font-size: 24px; color: #555; margin-bottom: 8px;
  }
  .contact__icon { width: 22px; height: 22px; flex: none; }
</style>
</head>
<body>
  <main class="sheet">
    <section class="card card--front" aria-label="Card front">
      <p class="brand-name">Lorna Tess<br>Tresses</p>
    </section>

    <section class="card card--back" aria-label="Card back">
      <p class="brand-name">Lorna Tess Tresses</p>
      <div class="divider"></div>
      <div class="contact">
        <p class="contact__name"><span class="first">Lorna</span> <span class="last">Tess</span></p>
        <p class="contact__role">Custom Wig Maker</p>
        <ul class="contact__list">
          <li class="contact__item">
            <svg class="contact__icon" viewBox="0 0 24 24" aria-hidden="true">
              <circle cx="12" cy="12" r="12" fill="#e34298"/>
              <path d="M8.2 6.5l2 .2 1 2.6-1.3 1.1a7 7 0 0 0 3.7 3.7l1.1-1.3 2.6 1 .2 2c-.6.8-1.6 1.2-2.6 1A10 10 0 0 1 7.2 9.1c-.2-1 .2-2 1-2.6z" fill="#fff"/>
            </svg>
            582 907 3365
          </li>
          <li class="contact__item">
            <svg class="contact__icon" viewBox="0 0 24 24" aria-hidden="true"><circle cx="12" cy="12" r="12" fill="#e34298"/></svg>
            @lorna.tess.tresses
          </li>
          <li class="contact__item">
            <svg class="contact__icon" viewBox="0 0 24 24" aria-hidden="true"><circle cx="12" cy="12" r="12" fill="#e34298"/></svg>
            www.lornatesstresses.example
          </li>
        </ul>
      </div>
    </section>
  </main>
</body>
</html>
```